Beekeeper needs a label for honey jars

Ciao! I'm from Como Italy
I'm a hobbyist beekeeper and I produce honey for myself and my friends.
I've named my apiary "Dado di sole," a play on words between my nickname (Dado, from Edoardo) and the Italian expression "Dado di sole," which translates to "a drizzle of honey" in English.
I need to create a label for my honey glass jars (250 gr and 500 gr).
I don't need a label for commercial purposes. I would like to include at least the name “Apicoltura Dado di sole", the type of honey (e.g., wildflower, acacia...) and a space for the production year, to be handwritten each year.
In the design some references to the world of bees.
For reference, attached a label with a style I like
Attached are the images of the selected jars and their measurements
Thanks and good job!

beekeeping, honey

• I would like an elegant style with clean graphics.
• Predominance of black color.

```html
<!DOCTYPE html>
<html lang="it">
<head>
<meta charset="utf-8">
<title>Apicoltura Dado di sole – etichetta miele</title>
<link rel="stylesheet" href="https://fonts.googleapis.com/css2?family=Newsreader:opsz,wght@6..72,400;6..72,500&family=Caveat:wght@400&family=Mrs+Saint+Delafield&display=swap">
<style>
  :root {
    --backdrop: #f2f1ee;
    --label: #ffffff;
    --ink: #1c1c1c;
    --ink-soft: #6b6b6b;
    --ink-mid: #3a3a3a;
    --pen-blue: #5563b8;
    --rule: #4a4a4a;
  }
  * { margin: 0; padding: 0; box-sizing: border-box; }
  html, body {
    width: 1200px; height: 1200px; overflow: hidden;
    background: var(--backdrop);
  }
  .label {
    position: absolute; left: 73px; top: 151px;
    width: 1054px; height: 898px;
    background: var(--label);
    box-shadow: 0 2px 10px rgba(0,0,0,0.06);
    color: var(--ink);
    font-family: "Newsreader", Georgia, serif;
  }
  .masthead {
    position: absolute; left: 0; right: 0; top: 120px;
    text-align: center; color: var(--ink);
    font-weight: 400;
  }
  .masthead .trade {
    display: block; font-size: 34px; letter-spacing: 10px;
    text-transform: uppercase; line-height: 1;
  }
  .masthead .name {
    display: block; margin-top: 34px;
    font-size: 104px; line-height: 1; letter-spacing: 0;
  }
  .bee-illustration {
    position: absolute; left: 320px; top: 372px; width: 420px; height: 316px;
  }
  .maker {
    position: absolute; left: 80px; top: 500px;
    font-family: "Mrs Saint Delafield", cursive;
    color: var(--ink-soft); transform: rotate(-8deg);
  }
  .maker .by { display: block; font-size: 30px; margin-left: 130px; }
  .maker .name { display: block; font-size: 60px; line-height: 0.9; }
  .variety {
    position: absolute; left: 0; right: 0; top: 738px; text-align: center;
  }
  .variety .kind { font-size: 58px; line-height: 1; color: var(--ink-mid); }
  .variety .note { font-size: 30px; margin-top: 6px; color: var(--ink); letter-spacing: 0.5px; }
  .field {
    position: absolute; top: 712px; width: 126px; text-align: center;
  }
  .field.year { left: 68px; }
  .field.weight { left: 860px; top: 700px; }
  .field .value {
    font-family: "Caveat", cursive; font-size: 44px; color: var(--pen-blue);
    line-height: 1; height: 54px;
  }
  .field .rule { border-top: 2px solid var(--rule); margin: 10px 0 14px; }
  .field .caption {
    font-size: 27px; color: var(--ink-mid); letter-spacing: 0.5px;
  }
</style>
</head>
<body>
  <main class="label">
    <h1 class="masthead">
      <span class="trade">Apicoltura</span>
      <span class="name">Dado di sole</span>
    </h1>

    <svg class="bee-illustration" role="img" aria-label="Illustrazione in bianco e nero di un'ape con ali aperte" viewBox="0 0 420 316">
      <defs>
        <radialGradient id="bee-tone" cx="50%" cy="50%" r="55%">
          <stop offset="0%" stop-color="#9a9a9a"/>
          <stop offset="100%" stop-color="#f1f1f1"/>
        </radialGradient>
      </defs>
      <ellipse cx="210" cy="158" rx="205" ry="150" fill="url(#bee-tone)"/>
    </svg>

    <div class="maker"><span class="by">da</span><span class="name">Edoardo</span></div>

    <div class="field year">
      <div class="value">2023</div>
      <div class="rule"></div>
      <div class="caption">ANNO</div>
    </div>

    <div class="variety">
      <p class="kind">fiore di campo</p>
      <p class="note">100% naturale</p>
    </div>

    <div class="field weight">
      <div class="value">250 g</div>
      <div class="rule"></div>
      <div class="caption">NETTO</div>
    </div>
  </main>
</body>
</html>
```